Innovative WordPress for a non-profit organization dedicated to providing healthcare to the less for

Bright Harbor Aid is a small non-profit organization. BHA's core mission is to provide free medical and dental care to the less fortunate. Aside from providing healthcare, BHA also helps build infrastructure such as orphanage, cancer centers, water wells and small homes for the homeless. As a non-profit, BHA has been sponsoring various social programs to help those in need. From building infrastructure to health care and most recently micro-finance, the BHA team is helping to GIve Back to the community at person at a time.

BHA is growing and needs help to restructure for the future. The corporate website design is the first step in a new branding strategy for the company.

BHA current website is divided into three specific target areas:
1. Mission: This area is dedicated to provide information about medical and dental mission hosted by BHA.

2. Infrastructure. This area is dedicated to provide information about infrastructure programs supported and completed by the BHA team. The projects includes orphanage, cancer centers. water wells, micro-finance, small homes for the homeless...etc.

3. Special Projects. This area is used to showcase specific short term projects which might come up.

Aside from the specific three target area, BHA also needs a NEWS area where news about BHA can be published.

Please put your thinking cape on and help produce the next generation WordPress template for Bright Harbor Aid. Your design will great enhance the level of volunteers recruited and also increase the level of help that BHA can provide for other.

For a quick glance at the BHA website today, please visit http://www.bhaexample.org. The BHA team is looking for a fresh design.

Thank you very much for taking the time to help BHA advance its mission of helping those in need.

Reason: Seeking more variety in design. Design needs to have a donate button, sponsors area, news, welcome message, 3 primary functions (mission, infrastructure, and specials projects). The BHA logo is available. Please note, you have the option to NOT use the colors associated with BHA logo. Thank you for helping with designing the new site.

Non-Profit

Requirements
Must have
• 1. Donate Now button.
2. Primary focus areas: MISSION / INFRASTRUCTURE / SPECIAL PROJECTS
3. News & Events
4. Welcome Message area
5. Sponsors area - place to add sponsor logos

Nice to have
• 1. Photo of the Month: Used to show a specific photo to represent events or functions completed by the BHA team.

Please show sample of one level down. For example, what does the page look like when I click the MISSION link.

```html
<!DOCTYPE html>
<html lang="en">
<head>
<meta charset="utf-8">
<title>Bright Harbor Aid</title>
<link href="https://fonts.googleapis.com/css2?family=Yanone+Kaffeesatz:wght@300;400;700&family=Open+Sans:wght@400;600&family=Arimo:wght@400;700&display=swap" rel="stylesheet">
<style>
:root{
  --green:#0a9a47;
  --yellow:#f7d417;
  --red:#ec1c24;
  --grey-box:#8a8a8a;
  --ink:#222;
  --body:#3a3a3a;
  --muted:#777;
  --band:#ececec;
  --page:#f7f6f3;
}
*{box-sizing:border-box;margin:0;padding:0}
html,body{width:897px;height:1200px;overflow:hidden}
body{position:relative;background:var(--page);font-family:"Arimo",Arial,sans-serif;color:var(--body)}
.abs{position:absolute}
.top-bar{left:0;top:0;width:897px;height:3px;display:flex}
.top-bar span{height:3px}
.header{left:0;top:3px;width:897px;height:104px;background:#fff}
.brand{left:89px;top:30px;display:flex;align-items:center;gap:8px}
.brand-mark{width:26px;height:26px;background:var(--green);border-radius:50%}
.brand-name{font-family:"Open Sans",sans-serif;font-weight:600;font-size:25px;color:var(--ink);letter-spacing:.5px}
.tagline{left:94px;top:78px;font-family:"Open Sans",sans-serif;font-size:8.5px;color:#666;letter-spacing:.4px}
.donate-top{left:663px;top:37px;width:132px;height:31px;background:var(--green);border-radius:2px;color:#fff;font-size:16px;display:flex;align-items:center;justify-content:center}
.nav{left:324px;top:84px;display:flex;font-family:"Open Sans",sans-serif;font-size:11.5px;color:var(--ink)}
.nav a{position:absolute;white-space:nowrap;color:inherit;text-decoration:none}
.nav .active::after{content:"";position:absolute;left:0;right:0;top:17px;height:3px;background:var(--green)}
.hatch{left:0;top:107px;width:897px;height:11px;background:repeating-linear-gradient(135deg,#e6e6e6 0 2px,#f4f4f4 2px 4px)}
.hero{left:96px;top:130px;width:704px;height:273px;background:linear-gradient(120deg,#5a4a3a 0%,#cfc6bb 35%,#e9e4dc 55%,#8d7f72 100%)}
.hero-caption{left:96px;top:340px;width:704px;height:63px;background:rgba(40,40,40,.78);color:#fff;font-family:"Yanone Kaffeesatz",sans-serif;padding:8px 21px}
.hero-caption b{display:block;font-weight:700;font-size:17px}
.hero-caption span{display:block;font-weight:300;font-size:19px;margin-top:1px}
.focus-band{left:0;top:406px;width:897px;height:111px;background:var(--band);border-top:1px solid #ddd;border-bottom:1px solid #ddd}
.focus{top:416px;width:250px;height:89px;color:#fff;box-shadow:0 6px 5px -3px rgba(0,0,0,.25)}
.focus .icon{position:absolute;left:16px;top:19px;width:48px;height:48px;border-radius:50%;background:#fff;display:flex;align-items:center;justify-content:center}
.focus h3{position:absolute;left:73px;top:6px;font-family:"Yanone Kaffeesatz",sans-serif;font-weight:300;font-size:21px}
.focus p{position:absolute;left:73px;top:32px;width:165px;font-size:9px;line-height:11px;height:33px;overflow:hidden}
.focus a{position:absolute;left:73px;top:68px;font-size:8px;color:#fff}
.statement{left:60px;top:527px;width:777px;text-align:center;font-family:"Yanone Kaffeesatz",sans-serif;font-weight:300;font-size:22px;line-height:25px;color:#444}
.donate-mid{left:379px;top:614px;width:139px;height:33px;border:1px solid #bbb;border-radius:2px;background:linear-gradient(#fff,#dcdcdc);font-family:"Yanone Kaffeesatz",sans-serif;font-size:20px;color:#333;display:flex;align-items:center;justify-content:center;box-shadow:0 2px 3px rgba(0,0,0,.15)}
.band-edge{left:0;top:659px;width:897px;height:1px;background:#ddd}
.section-title{font-size:21px;color:var(--ink)}
.events-title{left:0;top:669px;width:897px;text-align:center}
.event{top:705px;width:170px;height:163px;background:#fff;border:1px solid #ddd}
.event h4{position:absolute;left:7px;top:6px;font-family:"Yanone Kaffeesatz",sans-serif;font-weight:400;font-size:16px;color:#333}
.event .thumb{position:absolute;left:7px;top:28px;width:156px;height:76px}
.event p{position:absolute;left:7px;top:108px;width:156px;font-size:10.5px;line-height:13px;color:var(--muted)}
.event time{position:absolute;left:10px;top:143px;font-size:10px;font-weight:700;color:#222}
.event .more{position:absolute;right:-1px;bottom:-1px;width:69px;height:19px;background:var(--grey-box);color:#fff;font-size:10px;display:flex;align-items:center;justify-content:center}
.about-title{left:92px;top:898px}
.about-text{left:91px;top:932px;width:488px;font-size:9.3px;line-height:14.7px;color:#333;text-align:justify}
.about-text p+p{margin-top:14px}
.link{font-size:8px;color:var(--green);text-decoration:underline}
.news-title{left:613px;top:898px}
.news-item{left:613px;width:190px}
.news-item .date{position:absolute;left:0;top:0;font-size:15px;color:#aaa;line-height:14px;width:26px}
.news-item .date small{display:block;font-size:10px}
.news-item h5{position:absolute;left:30px;top:0;font-weight:400;font-size:11.5px;line-height:14px;color:#222;width:160px}
.news-item p{position:absolute;left:0;top:30px;font-size:9.3px;line-height:11.5px;color:#333;width:190px}
.footer-line{left:0;top:1140px;width:897px;height:11px;background:linear-gradient(#e9e9e9,#f6f6f6);border-top:1px solid #e0e0e0}
.footer-text{left:0;top:1163px;width:897px;text-align:center;font-family:"Open Sans",sans-serif;font-size:8.5px;color:#666}
.bottom-bar{left:0;top:1194px;width:897px;height:6px;background:#d6d6d6}
</style>
</head>
<body>
<div class="abs top-bar"><span style="width:327px;background:var(--green)"></span><span style="width:235px;background:var(--yellow)"></span><span style="flex:1;background:var(--red)"></span></div>

<header class="abs header"></header>
<div class="abs brand"><span class="brand-mark"></span><span class="brand-name">Bright Harbor Aid</span></div>
<div class="abs tagline">SERVING THE DISADVANTAGE COMMUNITY</div>
<div class="abs donate-top">DONATE NOW</div>
<nav class="abs nav">
  <a class="active" style="left:0">HOME</a>
  <a style="left:48px">ABOUT US</a>
  <a style="left:123px">MISSION</a>
  <a style="left:189px">SPECIAL PROJECTS</a>
  <a style="left:312px">INFRASTRUCTURE</a>
  <a style="left:429px">EVENTS</a>
</nav>
<div class="abs hatch"></div>

<div class="abs hero" role="img" aria-label="Photo of smiling dental clinic volunteers in white uniforms"></div>
<div class="abs hero-caption"><b>Dr. Mara Lind (far right) working with the volunteers at a BHA dental clinic.</b><span>Dr. Mara Lind mentoring a group of volunteers who will be future dentist at the BHA Dental Clinic.</span></div>

<div class="abs focus-band"></div>
<section class="abs focus" style="left:64px;background:var(--green)">
  <div class="icon"><svg width="26" height="26" viewBox="0 0 24 24"><path d="M22 2 2 10l7 3 3 8z" fill="#0a9a47"/><path d="M9 13l13-11" stroke="#fff" stroke-width="1.5"/></svg></div>
  <h3>Mission</h3>
  <p>Through the years, Bright Harbor Aid has hosted numerous different types of dental/medical missions. Most recently</p>
  <a>Learn more</a>
</section>
<section class="abs focus" style="left:324px;background:var(--grey-box)">
  <div class="icon"><svg width="26" height="26" viewBox="0 0 24 24" fill="#8a8a8a"><path d="M12 2 2 7v2h20V7z"/><rect x="4" y="10" width="3" height="8"/><rect x="10.5" y="10" width="3" height="8"/><rect x="17" y="10" width="3" height="8"/><rect x="2" y="19" width="20" height="3"/></svg></div>
  <h3>Infrastructure</h3>
  <p>Linh Son Cancer Center – Oak HouseAside from hosting various dental and medical missions through out the</p>
  <a>Learn more</a>
</section>
<section class="abs focus" style="left:584px;background:var(--red)">
  <div class="icon"><svg width="26" height="26" viewBox="0 0 24 24"><rect x="2" y="2" width="20" height="20" rx="4" fill="#ec1c24"/><path d="M10 5h4v5h5v4h-5v5h-4v-5H5v-4h5z" fill="#fff"/></svg></div>
  <h3>Special Projects</h3>
  <p>Linh Son Cancer Center – Oak HouseAside from hosting various dental and medical missions through out the</p>
  <a>Learn more</a>
</section>

<p class="abs statement">BHA's core mission is to provide free medical and dental care to the less fortunate. Aside from providing healthcare, BHA also helps build infrastructure such as orphanage, cancer centers, water wells and small homes for the homeless.</p>
<div class="abs donate-mid">Donate Now</div>
<div class="abs band-edge"></div>

<h2 class="abs section-title events-title">Featured Events</h2>
<article class="abs event" style="left:86px"><h4>Lorem ipsum dolor</h4><div class="thumb" role="img" aria-label="Photo of a child at a dental check-up" style="background:linear-gradient(90deg,#d9c7b0,#f1efe9 60%,#c9b9a8)"></div><p>Pellentesque habitant morbi tris-tique senectus et netus et</p><time>26 Mar, 2014</time><span class="more">Read More</span></article>
<article class="abs event" style="left:268px"><h4>Lorem ipsum dolor</h4><div class="thumb" role="img" aria-label="Photo of a doctor examining a patient" style="background:linear-gradient(90deg,#3b332c,#b9a896 50%,#6d5d4c)"></div><p>Pellentesque habitant morbi tris-tique senectus et netus et</p><time>20 April, 2014</time><span class="more">Read More</span></article>
<article class="abs event" style="left:452px"><h4>Lorem ipsum dolor</h4><div class="thumb" role="img" aria-label="Group photo of volunteers in green shirts" style="background:linear-gradient(#4e6b3a,#8dc63f 60%,#3f4a35)"></div><p>Pellentesque habitant morbi tris-tique senectus et netus et</p><time>12 may, 2014</time><span class="more">Read More</span></article>
<article class="abs event" style="left:635px"><h4>Lorem ipsum dolor</h4><div class="thumb" role="img" aria-label="Dental clinic sponsors banner" style="background:linear-gradient(#8fb4d8,#dcd6c8 60%,#b9ab95)"></div><p>Pellentesque habitant morbi tris-tique senectus et netus et</p><time>10 Jun, 2014</time><span class="more">Read More</span></article>

<h2 class="abs section-title about-title">About us</h2>
<div class="abs about-text">
  <p>Bright Harbor Aid (BHA) is a non-profit 501(c)(3) organization dedicated to providing health-care, human services, and educational assistance to underprivileged communities. We work in collaboration with various groups and non-governmental organizations (NGOs) to deliver humanitarian goods, services, and relief to impoverished regions. The team is comprised of professionals with a broad spectrum of experiences. The combined mission trips of our team span across North America, South America, South Africa, and South East Asia, bringing a variety of general and specialized disciplines to each region.</p>
  <p>The BHA Team's initial medical mission project was to Phnom Penh, Cambodia in March 2005. The mission team provided care to over 2,500 patients. In November 2005, the BHA Team collaborated with Coastal Assistance for the Disabled (CAD) to bring a Medical, Dental, and Public Health mission to Da Nang, Vietnam. This medical mission provided treatments to over 2,700 students from first to fifth grades.</p>
  <p class="link" style="margin-top:10px">More info</p>
</div>

<h2 class="abs section-title news-title">Latest News</h2>
<div class="abs news-item" style="top:948px"><span class="date">10<small>JUN</small></span><h5>Lorem ipsum dolor sit amet consectetur</h5><p>Fusce diam mauris, pulvinar a nulla vitae, ornare sagittis leo.</p></div>
<div class="abs news-item" style="top:1019px"><span class="date">16<small>MAY</small></span><h5>Lorem ipsum dolor sit amet consectetur</h5><p>Fusce diam mauris, pulvinar a nulla vitae, ornare sagittis leo.Lorem ipsum dolor sit amet</p></div>
<a class="abs link" style="left:613px;top:1090px">More info</a>

<div class="abs footer-line"></div>
<footer class="abs footer-text">© 2014 Bright Harbor Aid</footer>
<div class="abs bottom-bar"></div>
</body>
</html>
```